Pagecraft Design Project - Vibrant Children's school bag website

We need a fresh design for the landing page of our new web site and blog: quillonmarket.com

Tamborine specialises in supplying schools all over the world and now also parents directly with, personalised school bags, accessories, crafts and gifts for their children.

I have attached the visual that our web designers have provided so that we can see the layout of the various window, but now we need to add the personal touch of making it our own and visually making the site look enticing and exciting to shop on.
Updates

Hello Designers,

We are now in the final round of choosing a design.  We have found that most deisgns are very similar and that none are completley original.  Therefore, we are willing to throw our wire frame away and start with a compleltely new visual so you can design what ever you like!

The only requirements we have is that we must have:
- A large rolling banner to show our products lines
- Our Company logo
- Meta going tags across the top
- Icons for chatterbook,snipboard,blog,
- Account Login bar
- A log in area for schools
- A login area to register for the Club Tambo

So we are looking for something that really stands out from the crowd!

can you deliver?

Thanks,

Target Market(s)

To appeal to mum's shopping on line for their children's school items and gifts.

Industry/Entity Type

School

Requirements
Must have
• -When you see the visual attached please note the amendments:
- the word 'school bags' under our company name will not appear
- the tag line "Australia's no 1 specialist school bag company' should be deleted. We will leave this area open so that you can include some simple icons that we would like featured across the top of the banner i.e:
- a love heart icon + wording to say : Made with love
- A 'delivery' icon + wording to say : Free delivery
- A 'warranty' icon + wording to say : up to 25 year warranty
- A 'world' icon + wording to say : we ship to the universe
(Please see: www.pebblecrate.com.au for reference of what we mean!)

We we want the overall design to be clean, fresh, crisp and fun to look at.

You may alter the colours of everything, even the coloured tabs. we think that the coloured tabs should actually just be one colour through out and to let the tamborine name stand out with all it's.

The top/main photo will be a rolling banner.

You can change the shapes of the boxes but keep to the wire frame.

Please alter the design of the black/coloured club tambo card to suit your design.

Our aim is to also change the side panels in peak seasons to reflect halloween banner, christmas banner etc.

Please see my screen shot of the current page and see where the "dots' pattern sits on either side of the shopping panels. Please include the side panels as we want to change the design to have themes i.e for halloween, for christmas etc etc.

example of websites that have this:

http://www.wavemoorly.com/

Please include a 'blog' and snipboard icon.

The site will not only manage our retail sales but will also be a portal for our schools to register and place their bulk orders with us. So the "wholesale register box" must stand out so our school customers can easily see where they need to click & register.
Should not have
• Please do not do a 'baby' boutique theme. We need a theme that appeals to mum's that have children across the ages of 3-14 years.

```html
<!DOCTYPE html>
<html lang="en">
<head>
<meta charset="utf-8">
<title>Tamborine – School Bags, Crafts &amp; Gifts</title>
<link href="https://fonts.googleapis.com/css2?family=Fredoka:wght@600&family=Varela+Round&family=Open+Sans:wght@400;600;700&family=Dancing+Script:wght@600&display=swap" rel="stylesheet">
<style>
:root{
  --bg:#ececec;
  --sky:#7ec8ea;
  --sky-pale:#b5e1f4;
  --sky-deep:#3a9fd0;
  --green:#8cc63f;
  --green-dark:#6aa321;
  --green-pale:#b6dd6e;
  --orange:#ff9a1e;
  --orange-dark:#f27e00;
  --orange-line:#f6c98c;
  --yellow:#f6d100;
  --ink:#333;
  --ink-soft:#555;
  --blue-link:#1a7bbf;
  --red:#d9262c;
  --footer:#c2c8cb;
  --footer-edge:#8a8f92;
  --purple:#8a3fb0;
  --logo:#e8457a;
}
*{box-sizing:border-box;margin:0;padding:0}
html,body{width:1200px;height:1017px;overflow:hidden;background:var(--bg)}
body{font-family:"Open Sans",sans-serif;color:var(--ink)}
.page{position:relative;width:1100px;height:932px;transform:scale(1.0909);transform-origin:0 0;
  background:repeating-linear-gradient(45deg,#efefef 0 2px,#e8e8e8 2px 4px)}
.abs{position:absolute}
.topline{left:0;top:0;width:1100px;height:5px;background:var(--sky)}

.brand{left:207px;top:8px;font-family:"Fredoka",sans-serif;font-weight:600;font-size:44px;color:var(--logo);letter-spacing:-1px}
.perks{left:428px;top:38px;display:flex;gap:20px;align-items:center}
.perk{display:flex;align-items:center;gap:4px;font-size:10px;color:#555;line-height:1.05}
.perk b{font-family:"Varela Round",sans-serif;font-size:12px;color:#444}
.perk .script{font-family:"Dancing Script",cursive;font-size:12px;color:#444}
.perk .green{color:var(--green-dark)}

.login-tab{left:815px;top:0;width:80px;height:38px;background:linear-gradient(#c9ebf8,var(--sky-pale));border:1px solid var(--sky-deep);border-top:none;text-align:center;font-size:9px;color:#124;padding-top:2px}

.nav{left:205px;top:98px;width:688px;height:29px;background:linear-gradient(var(--green-pale),var(--green));display:flex;align-items:center;border-bottom:2px solid var(--green-dark)}
.nav .home{width:38px;height:100%;display:flex;align-items:center;justify-content:center}
.nav a{font-size:10px;color:#222;text-decoration:none;padding:0 8px;border-left:1px solid #3d5e14;line-height:12px;white-space:nowrap}
.nav a.strong{font-weight:700}

.banner{left:205px;top:127px;width:688px;height:306px;background:#fff}
.banner .photo{position:absolute;left:8px;top:7px;width:668px;height:292px;overflow:hidden;
  background:linear-gradient(90deg,#e7e7e7 0%,#d9d9d9 30%,#c9a48f 45%,#d9d9d9 58%,#c8403a 78%,#e5e5e5 100%)}
.banner .ribbon{position:absolute;left:0;top:0}
.arrow{width:26px;height:24px;background:linear-gradient(#e3e3e3,#bcbcbc);color:#fff;font-size:16px;text-align:center;line-height:22px;box-shadow:1px 1px 2px #999}
.cart{left:876px;top:157px;width:36px;height:82px;background:var(--sky-pale);border:1px solid var(--sky-deep);border-radius:4px;text-align:center;font-size:8px;color:#124;padding-top:6px;line-height:1.6}

.card{background:#fff;border:1px solid var(--orange-line)}
.card .inner{position:absolute;left:7px;top:8px;right:7px;bottom:7px;background:linear-gradient(#fff,#ececec)}
.card h2{position:absolute;left:7px;right:7px;top:8px;height:23px;background:linear-gradient(var(--orange),var(--orange-dark));font-family:"Varela Round",sans-serif;font-weight:400;font-size:15px;color:#4a2b00;text-align:center;line-height:23px}

.endorse .portrait{position:absolute;left:17px;top:40px;width:48px;height:62px;border:2px solid #fff;box-shadow:0 0 2px #888;background:linear-gradient(#e9eef2,#9db3c2)}
.endorse .who{position:absolute;left:76px;top:40px;font-size:9px;color:#3d8a1c}
.endorse .role{position:absolute;left:76px;top:53px;font-size:9px;font-weight:700;color:var(--blue-link)}
.endorse .quote{position:absolute;left:74px;top:67px;width:142px;font-size:7px;line-height:1.3;color:#444}
.go{position:absolute;width:10px;height:10px;border-radius:50%;background:var(--green-dark);color:#fff;font-size:7px;line-height:10px;text-align:center}
.go.y{background:var(--yellow)}

.social{position:absolute;top:52px;display:flex;flex-direction:column;align-items:center;gap:4px;font-size:8px;color:#555}
.social span.dot{width:48px;height:48px;border-radius:50%;display:flex;align-items:center;justify-content:center;color:#fff;font-size:7px;font-weight:700}

.club .join{position:absolute;left:7px;top:31px;width:211px;height:32px;background:var(--yellow);font-size:9px;padding:4px 0 0 18px;line-height:1.15;color:#222}
.club .join b{font-size:12px}
.club .email{position:absolute;left:12px;top:70px;width:107px;height:18px;border:1px solid #777;border-radius:3px;background:#fff;font-size:9px;text-align:center;line-height:16px;color:#444}
.club .btn{position:absolute;left:14px;top:95px;width:53px;height:13px;background:linear-gradient(#9fd9f5,var(--sky-deep));border-radius:2px;font-size:8px;color:#124;text-align:center;line-height:13px}
.club .member{position:absolute;left:126px;top:74px;width:84px;height:50px;border-radius:5px;transform:rotate(-10deg);background:linear-gradient(135deg,#f7a74a,#e07a14);box-shadow:1px 2px 3px #888}

.community .partner{position:absolute;left:0;right:0;top:55px;text-align:center;font-family:"Varela Round",sans-serif;font-size:14px;color:#5a3a2a}

.news h2{text-align:left;padding-left:48px}
.news .blogmark{position:absolute;left:18px;top:10px;width:20px;height:20px;border-radius:50%;background:#fff;border:2px solid var(--purple)}
.news .col{position:absolute;top:40px;width:94px;height:83px;padding-left:12px}
.news .col + .col{border-left:1px solid #999}
.news .col h3{font-size:10px;font-weight:700;color:#555;margin-bottom:10px}
.news .col p{font-size:8px;line-height:1.55;color:#222}

.schools{background:#fff;border:1px solid #b77dd0}
.schools .panel{position:absolute;left:3px;top:6px;width:127px;height:125px;background:linear-gradient(#7cd0f6,#27b0e6)}
.schools .title{position:absolute;left:15px;top:14px;font-family:"Varela Round",sans-serif;color:#123;line-height:1.15;font-size:16px}
.schools .title small{font-size:12px}
.schools .reg{position:absolute;left:32px;top:85px;width:95px;height:20px;background:linear-gradient(90deg,#f2632a,#a3279e);color:#fff;font-size:10px;line-height:20px;text-align:center}

.follow{left:206px;top:742px;width:543px;height:26px;background:#fff;border:1px solid #c4a6d8;display:flex;align-items:center;font-size:10px}
.follow .label{color:var(--red);font-weight:700;font-size:11px;margin:0 6px 0 8px}
.chip{display:inline-block;width:17px;height:17px;border-radius:3px;margin-right:4px}
.follow .secure{margin-left:40px;display:flex;align-items:center;gap:3px}
.follow .pay{margin-left:32px;font-weight:700;font-size:11px}
.paychip{display:inline-block;min-width:24px;height:14px;border:1px solid #bbb;font-size:6px;line-height:12px;text-align:center;margin-left:4px;padding:0 2px;color:#235}

.footer{left:207px;top:777px;width:542px;height:134px;background:var(--footer);border:2px solid var(--footer-edge)}
.footer .col{position:absolute;top:4px}
.footer h4{font-family:"Varela Round",sans-serif;font-weight:400;font-size:11px;color:#222;border-bottom:1px dashed #666;display:inline-block;margin-bottom:6px}
.footer li{list-style:none;font-size:8px;color:#444;line-height:15px;padding-left:12px;position:relative}
.footer li::before{content:"✓";position:absolute;left:0;color:#b0308a;font-size:9px}

.seasonal{left:760px;top:742px;width:133px;height:169px;background:linear-gradient(#a6d46a,#5f9a1f);color:#fff;font-family:"Varela Round",sans-serif;text-align:center;padding-top:32px;line-height:1.2}
.seasonal .s1{font-size:21px}
.seasonal .s2{font-size:33px}
.copy{left:209px;top:915px;font-size:8px;color:#222}
</style>
</head>
<body>
<div class="page">
  <div class="abs topline"></div>

  <div class="abs brand">tamborine</div>

  <div class="abs perks">
    <div class="perk">
      <svg width="26" height="22" viewBox="0 0 26 22"><path d="M13 20 C4 13 1 9 3 5 C5 1 10 2 13 6 C16 2 21 1 23 5 C25 9 22 13 13 20Z" fill="none" stroke="#5a9b2b" stroke-width="2"/></svg>
      <span class="script">Made with Love</span>
    </div>
    <div class="perk">
      <svg width="40" height="26" viewBox="0 0 40 26"><rect x="1" y="5" width="22" height="14" fill="#7cbf25"/><path d="M23 9h9l6 6v4H23z" fill="#5a9b2b"/><circle cx="9" cy="21" r="3.5" fill="#333"/><circle cx="31" cy="21" r="3.5" fill="#333"/></svg>
      <span><b>free</b><br><span class="green">Delivery</span></span>
    </div>
    <div class="perk">
      <svg width="30" height="30" viewBox="0 0 30 30"><circle cx="15" cy="15" r="13" fill="#7cbf25" stroke="#4a7d18" stroke-width="2"/><text x="15" y="20" font-size="13" font-family="Varela Round,sans-serif" fill="#fff" text-anchor="middle">25</text></svg>
      <span><b>Years</b><br><span class="green">Warranty</span></span>
    </div>
    <div class="perk">
      <svg width="32" height="32" viewBox="0 0 32 32"><circle cx="16" cy="16" r="14" fill="#8cc63f"/><ellipse cx="16" cy="16" rx="6" ry="14" fill="none" stroke="#fff" stroke-width="1.5"/><path d="M2 16h28M4 9h24M4 23h24" stroke="#fff" stroke-width="1.5"/></svg>
      <span><b>We Ship</b><br><span class="green">to the Universe</span></span>
    </div>
  </div>

  <div class="abs login-tab">
    <svg width="22" height="20" viewBox="0 0 22 20"><path d="M4 16 L16 4 L19 7 L7 19 L3 19Z" fill="none" stroke="#124" stroke-width="1.6"/></svg><br>Account Login
  </div>

  <nav class="abs nav">
    <span class="home"><svg width="18" height="16" viewBox="0 0 18 16"><path d="M1 8 L9 1 L17 8 M3 7 V15 H15 V7" fill="none" stroke="#fff" stroke-width="2"/></svg></span>
    <a>Kids Backpacks</a><a class="strong">Kids Bags</a><a>Sports</a><a class="strong">Kids Clothing</a><a>Art &amp; Craft</a><a>Music</a><a>Kids Diaries</a><a>Kids Storage</a><a class="strong">Extra Stuff</a><a class="strong">Sale</a>
  </nav>

  <section class="abs banner">
    <div class="photo" role="img" aria-label="Rolling banner photo: a mother fitting a yellow school backpack on her son">
      <svg class="ribbon" width="170" height="170" viewBox="0 0 170 170">
        <polygon points="0,124 124,0 158,0 0,158" fill="#b5e1f4"/>
        <text x="72" y="83" transform="rotate(-45 72 83)" text-anchor="middle" font-family="Varela Round, sans-serif" font-size="15" fill="#4aa6cf">Lorem ipsum dolor sit</text>
      </svg>
    </div>
  </section>
  <div class="abs arrow" style="left:200px;top:294px">«</div>
  <div class="abs arrow" style="left:883px;top:294px">»</div>
  <div class="abs cart">
    <svg width="22" height="18" viewBox="0 0 22 18"><path d="M1 2h4l3 10h11l2-7H7" fill="none" stroke="#124" stroke-width="1.5"/><circle cx="9" cy="15" r="1.6" fill="#124"/><circle cx="17" cy="15" r="1.6" fill="#124"/></svg><br>Items<br><b>0 0</b>
  </div>

  <section class="abs card endorse" style="left:207px;top:446px;width:226px;height:140px">
    <div class="inner"></div>
    <h2>Endorsement</h2>
    <div class="portrait" role="img" aria-label="Portrait of the endorsing chiropractor"></div>
    <div class="who">Dr Lena Marsh</div>
    <div class="role">Chiropractor &amp; Osteopath</div>
    <p class="quote">"Choosing the correct backpack for your child to start the school year with isan important decision for any parent to make. Importantly, your school backpack should be ergo-nomic and light to carry...</p>
    <span class="go" style="left:202px;top:117px">›</span>
  </section>

  <section class="abs card" style="left:437px;top:446px;width:226px;height:140px">
    <div class="inner"></div>
    <h2>Say to Tamborine</h2>
    <div class="social" style="left:32px"><span class="dot" style="background:#3b5a9a">chatterbook</span></div>
    <div class="social" style="left:89px"><span class="dot" style="background:#2aa7dc">Chirply</span></div>
    <div class="social" style="left:145px"><span class="dot" style="background:#9a9a9a">Streamly</span></div>
  </section>

  <section class="abs card club" style="left:668px;top:446px;width:225px;height:140px">
    <div class="inner"></div>
    <h2>Club Tambo</h2>
    <div class="join"><b>Join Now</b> for 15% off on<br>your 1st order!*</div>
    <div class="email">email address</div>
    <div class="btn">Join »</div>
    <div class="member" role="img" aria-label="Club Tambo membership card"></div>
  </section>

  <section class="abs card community" style="left:207px;top:597px;width:136px;height:140px">
    <div class="inner"></div>
    <h2>Community</h2>
    <div class="partner">Kindred Hands</div>
  </section>

  <section class="abs card news" style="left:350px;top:597px;width:399px;height:140px">
    <div class="inner"></div>
    <h2>News &amp; Blog</h2>
    <span class="blogmark"></span>
    <div class="col" style="left:8px"><h3>Headline1</h3><p>Lorem ipsum dolor sit amet, consectetur adipisicing elit, sed do eiusmod tempor .</p></div>
    <div class="col" style="left:104px"><h3>Headline2</h3><p>Lorem ipsum dolor sit amet, consectetur adipisicing elit, sed do eiusmod tempor .</p></div>
    <div class="col" style="left:200px"><h3>Headline3</h3><p>Lorem ipsum dolor sit amet, consectetur adipisicing elit, sed do eiusmod tempor .</p></div>
    <div class="col" style="left:294px"><h3>Headline4</h3><p>Lorem ipsum dolor sit amet, consectetur adipisicing elit, sed do eiusmod tempor .</p></div>
    <span class="go y" style="left:87px;top:114px">›</span>
    <span class="go y" style="left:176px;top:114px">›</span>
    <span class="go y" style="left:269px;top:114px">›</span>
    <span class="go y" style="left:365px;top:114px">›</span>
  </section>

  <section class="abs schools" style="left:758px;top:597px;width:135px;height:140px">
    <div class="panel"></div>
    <div class="title"><small>Schools</small><br>&amp; Resellers<br>Registration</div>
    <div class="reg">Register Now</div>
  </section>

  <div class="abs follow">
    <span class="label">Follow Us on</span>
    <span class="chip" style="background:#3b5a9a"></span><span class="chip" style="background:#2aa7dc"></span><span class="chip" style="background:#c4302b"></span><span class="chip" style="background:#b8282f"></span>
    <span class="secure"><svg width="18" height="18" viewBox="0 0 18 18"><path d="M2 10 L7 15 L16 2" fill="none" stroke="#5a9b2b" stroke-width="2.5"/></svg>100% Secured</span>
    <span class="pay">Payment Options</span>
    <span class="paychip">Cardo</span><span class="paychip">Monvo</span><span class="paychip">Axiom</span><span class="paychip">PayLoop</span>
  </div>

  <footer class="abs footer">
    <div class="col" style="left:28px"><h4>Tamborine Gurantee</h4><ul><li>Delivery Gurantee</li><li>Pricing Gurantee</li><li>Privacy Gurantee</li><li>Return Gurantee</li><li>Security Gurantee</li></ul></div>
    <div class="col" style="left:169px"><h4>What's in Store</h4><ul><li>Lorem ipsum dolor sit</li><li>Lorem ipsum dolor sit</li><li>Lorem ipsum dolor sit</li><li>Lorem ipsum dolor sit</li><li>Lorem ipsum dolor sit</li></ul></div>
    <div class="col" style="left:296px"><h4>Want our Help ?</h4><ul><li>Contact Us</li><li>About Us</li><li>My Account</li><li>Policies</li><li>FAQ</li></ul></div>
    <div class="col" style="left:424px"><h4>Other Information</h4><ul><li>Lorem Ipsum dolor sit</li><li>Lorem Ipsum dolor sit</li><li>Lorem Ipsum dolor sit</li><li>Lorem Ipsum dolor sit</li><li>Lorem Ipsum dolor sit</li></ul></div>
  </footer>

  <aside class="abs seasonal"><div class="s1">Seasonal</div><div class="s2">Sales</div></aside>

  <div class="abs copy">© Copyright tamborine.com</div>
</div>
</body>
</html>
```